Financial Planning firm focused on serving women 55-65 yrs old needs stationary design

We are rebranding our financial planning firm and our target client is a 55-65 yr old women. We need a stationary design to go with our new logo.

Contact Information: Harold Brunsett, MS, CFP President Brunsett Wealth Management 48210 Marlowe Crest Drive, Suite 517 Estero, FL 33928 hal@brunsettwealthgrp.com phone 239-584-0139

```html
<!DOCTYPE html>
<html lang="en">
<head>
<meta charset="utf-8">
<title>Brunsett Wealth Management – Stationery Set 1</title>
<link href="https://fonts.googleapis.com/css2?family=Roboto+Condensed:wght@400;700&family=PT+Sans&display=swap" rel="stylesheet">
<style>
:root{
  --board:#545454;
  --paper:#ffffff;
  --navy:#2a6591;
  --sage:#9eb59e;
  --mist:#dde2ec;
  --ghost:#eef1ef;
  --ink:#222;
  --caption:#f2f2f2;
}
*{margin:0;padding:0;box-sizing:border-box}
html,body{width:1200px;height:1000px;overflow:hidden;background:var(--board)}
body{position:relative;font-family:"Roboto Condensed",Arial,sans-serif;color:var(--ink)}
.piece{position:absolute;background:var(--paper);overflow:hidden}
.piece.navy{background:var(--navy)}
.card{width:265px;height:164px}
.art{position:absolute;left:0;top:0}
.disc{position:absolute;border-radius:50%}
.holder{position:absolute;right:26px;text-align:right;color:var(--navy)}
.holder .name{font-weight:700;font-size:12px;letter-spacing:.2px}
.holder .role{font-size:7px;color:#333;margin-top:1px}
.navy .holder,.navy .holder .role{color:#fff}
.contacts{position:absolute;list-style:none;font-size:7px;line-height:12.5px;color:#222}
.navy .contacts{color:#fff}
.contacts li{display:flex;align-items:center;gap:3px;white-space:nowrap}
.ico{display:inline-block;width:7px;height:8px;border-radius:1.5px;background:var(--navy)}
.navy .ico{background:#fff}
.brand{position:absolute;display:flex;align-items:center}
.brand .wordmark{color:var(--navy);font-weight:400;line-height:1;text-transform:uppercase}
.brand .wordmark small{display:block;font-size:.24em;letter-spacing:.5px;margin-top:3px}
.navy .brand .wordmark{color:#fff}
.caption{position:absolute;left:595px;top:830px;font-family:"PT Sans",Arial,sans-serif;font-size:17px;line-height:23.5px;color:var(--caption)}
</style>
</head>
<body>

<!-- Card 1 front -->
<section class="piece card" style="left:22px;top:17px">
  <div class="disc" style="left:200px;top:73px;width:124px;height:124px;background:var(--sage)" role="img" aria-label="Large tree emblem area"></div>
  <div class="holder" style="top:14px"><div class="name">Colin Harte</div><div class="role">Owner/ Founder</div></div>
  <ul class="contacts" style="left:20px;top:87px">
    <li><span class="ico"></span>001427.5316</li>
    <li><span class="ico"></span>001427.5316</li>
    <li><span class="ico"></span>mail204@postvale.com</li>
    <li><span class="ico"></span>site@postvale.com</li>
    <li><span class="ico"></span>000 Ridge Lane, Hollow Bend NSW 2791</li>
  </ul>
</section>

<!-- Card 1 back -->
<section class="piece card navy" style="left:304px;top:17px">
  <div class="brand" style="left:30px;top:46px;gap:10px">
    <span class="disc" style="position:static;width:68px;height:68px;background:#fff"></span>
    <span class="wordmark" style="font-size:34px">Brunsett<small>Wealth Management</small></span>
  </div>
</section>

<!-- Card 2 front -->
<section class="piece card navy" style="left:22px;top:197px">
  <div class="disc" style="left:-70px;top:12px;width:148px;height:148px;background:var(--mist)" role="img" aria-label="Tree emblem area"></div>
  <div class="holder" style="top:14px"><div class="name">Colin Harte</div><div class="role">Owner/ Founder</div></div>
  <ul class="contacts" style="left:92px;top:99px">
    <li><span class="ico"></span>0427531690</li>
    <li><span class="ico"></span>mail204@postvale.com</li>
    <li><span class="ico"></span>site@postvale.com</li>
    <li><span class="ico"></span>482 Ridge Lane, Hollow Bend NSW 2791</li>
  </ul>
</section>

<!-- Card 2 back -->
<section class="piece card" style="left:304px;top:197px">
  <div class="brand" style="left:28px;top:45px;gap:10px">
    <span class="disc" style="position:static;width:70px;height:70px;background:var(--sage)"></span>
    <span class="wordmark" style="font-size:34px">Brunsett<small>Wealth Management</small></span>
  </div>
</section>

<!-- Card 3 front -->
<section class="piece card" style="left:22px;top:378px">
  <svg class="art" width="265" height="164" viewBox="0 0 265 164">
    <path d="M0 0H50Q14 60 24 164H0Z" fill="var(--sage)"/>
    <path d="M30 72Q38 138 122 164H92Q46 132 30 72Z" fill="var(--navy)"/>
  </svg>
  <div class="holder" style="top:15px"><div class="name">Colin Harte</div><div class="role">Owner/ Founder</div></div>
  <ul class="contacts" style="left:142px;top:89px">
    <li><span class="ico"></span>001427.5316</li>
    <li><span class="ico"></span>001427.5316</li>
    <li><span class="ico"></span>mail204@postvale.com</li>
    <li><span class="ico"></span>site@postvale.com</li>
    <li><span class="ico"></span>000 Ridge Lane, Hollow</li>
  </ul>
</section>

<!-- Card 3 back -->
<section class="piece card" style="left:304px;top:378px">
  <svg class="art" width="265" height="164" viewBox="0 0 265 164">
    <path d="M0 0H50Q14 60 24 164H0Z" fill="var(--sage)"/>
    <path d="M30 72Q38 138 122 164H92Q46 132 30 72Z" fill="var(--navy)"/>
  </svg>
  <div class="brand" style="left:58px;top:50px;gap:8px">
    <span class="disc" style="position:static;width:62px;height:62px;background:var(--sage)"></span>
    <span class="wordmark" style="font-size:29px">Brunsett<small>Wealth Management</small></span>
  </div>
</section>

<!-- Envelope front -->
<section class="piece" style="left:26px;top:556px;width:443px;height:204px">
  <svg class="art" width="443" height="204" viewBox="0 0 443 204">
    <path d="M0 0H44Q14 80 27 204H0Z" fill="var(--sage)"/>
    <path d="M24 90Q36 170 98 204H64Q32 160 24 90Z" fill="var(--navy)"/>
  </svg>
  <div class="disc" style="left:364px;top:58px;width:130px;height:130px;background:#e8e8e8" role="img" aria-label="Faint tree emblem area"></div>
  <div class="brand" style="left:52px;top:19px;gap:6px">
    <span class="disc" style="position:static;width:44px;height:44px;background:var(--sage)"></span>
    <span class="wordmark" style="font-size:22px">Brunsett<small>Wealth Management</small></span>
  </div>
  <ul class="contacts" style="left:101px;top:66px;font-size:5px;line-height:7px">
    <li><span class="ico" style="width:5px;height:5px"></span>001427.5316</li>
    <li><span class="ico" style="width:5px;height:5px"></span>mail204@postvale.com</li>
    <li><span class="ico" style="width:5px;height:5px"></span>site@postvale.com</li>
    <li style="color:var(--navy)">000 Ridge Lane, Hollow Bend</li>
  </ul>
</section>

<!-- Envelope back -->
<section class="piece" style="left:26px;top:776px;width:443px;height:204px">
  <svg class="art" width="443" height="64" viewBox="0 0 443 64">
    <path d="M0 0H443V40Q443 62 420 62H23Q0 62 0 40Z" fill="var(--sage)"/>
  </svg>
  <div class="disc" style="left:198px;top:8px;width:48px;height:48px;background:#fff"></div>
</section>

<!-- Letterhead -->
<section class="piece" style="left:590px;top:17px;width:590px;height:762px">
  <svg class="art" width="590" height="762" viewBox="0 0 590 762">
    <path d="M0 0H50Q24 300 64 762H0Z" fill="var(--sage)"/>
    <path d="M31 330Q36 600 118 762H76Q40 600 31 330Z" fill="var(--navy)"/>
  </svg>
  <div class="disc" style="left:170px;top:283px;width:270px;height:270px;background:var(--ghost)" role="img" aria-label="Faint tree emblem area"></div>
  <div class="brand" style="left:375px;top:26px;gap:7px">
    <span class="disc" style="position:static;width:60px;height:60px;background:var(--sage)"></span>
    <span class="wordmark" style="font-size:30px">Brunsett<small>Wealth Management</small></span>
  </div>
  <ul class="contacts" style="left:141px;top:720px">
    <li><span class="ico"></span>001427.5316</li>
    <li><span class="ico"></span>mail204@postvale.com</li>
  </ul>
  <div style="position:absolute;left:244px;top:716px;width:1px;height:32px;background:#bbb"></div>
  <ul class="contacts" style="left:251px;top:720px">
    <li><span class="ico"></span>site@postvale.com</li>
    <li style="color:var(--navy);font-weight:700"><span class="ico"></span>000 Ridge Lane, Hollow Bend NSW 2791</li>
  </ul>
</section>

<div class="caption">
  Stationery Design for BRUNSETT<br>
  Set 1<br>
  Business card: 3 front 3 back options<br>
  Letterhead<br>
  Envelope: Front and back
</div>

</body>
</html>
```